Business Card Design

I'm after a modern and artistic business card design, with clean lines and popping colour. The business card should be professional looking and promote my business.

```html
<!DOCTYPE html>
<html lang="en">
<head>
<meta charset="utf-8">
<title>Alina Qasmi — Makeup Artist Business Card</title>
<link rel="stylesheet" href="https://fonts.googleapis.com/css2?family=Cormorant+Garamond:ital,wght@1,700&family=Cormorant+SC:wght@600&family=Tinos&display=swap">
<style>
  :root {
    --backdrop: #2a2a2c;
    --card-white: #ffffff;
    --card-black: #0b0b0b;
    --card-black-soft: #2b2b2b;
    --ink-brown: #5a3a2e;
    --ink-red: #8a2a1c;
    --ink-dark: #161616;
    --rule-grey: #6d6d6d;
    --lip-red: #c8141c;
    --skin: #e9d3cc;
    --lipstick-case: #5a3b30;
  }
  * { margin: 0; padding: 0; box-sizing: border-box; }
  html, body {
    width: 1200px; height: 749px; overflow: hidden;
    background: var(--backdrop);
  }
  .canvas {
    position: relative; width: 1200px; height: 749px;
    display: flex; align-items: center; justify-content: center; gap: 60px;
  }
  .card {
    position: relative; width: 540px; height: 309px; overflow: hidden;
    box-shadow: 0 14px 30px rgba(0,0,0,.45);
  }

  /* Back side */
  .card-back {
    background: linear-gradient(160deg, var(--card-black-soft) 0%, var(--card-black) 45%, var(--card-black) 100%);
  }
  .card-back .portrait {
    position: absolute; top: 0; right: 0; width: 150px; height: 190px;
    background: linear-gradient(160deg, var(--skin) 0%, var(--skin) 35%, var(--lip-red) 60%, #8d0c12 100%);
  }
  .card-back .write-line {
    position: absolute; left: 70px; width: 300px; height: 2px;
    background: var(--rule-grey);
  }
  .card-back .write-line.first { top: 228px; }
  .card-back .write-line.second { top: 262px; }

  /* Front side */
  .card-front { background: var(--card-white); }
  .card-front .lipstick {
    position: absolute; top: 22px; right: 34px; width: 150px; height: 96px;
    background: linear-gradient(200deg, var(--lipstick-case) 0%, var(--lipstick-case) 55%, var(--lip-red) 56%, #a10f16 100%);
    border-radius: 6px;
  }
  .card-front .identity {
    position: absolute; top: 74px; left: 34px; width: 300px;
  }
  .card-front .name {
    font-family: "Cormorant Garamond", serif; font-style: italic; font-weight: 700;
    font-size: 44px; line-height: 1; color: var(--ink-brown); letter-spacing: .5px;
  }
  .card-front .name-rule {
    height: 1px; background: var(--ink-brown); margin-top: 4px;
  }
  .card-front .role {
    font-family: "Cormorant SC", serif; font-weight: 600;
    font-size: 16px; letter-spacing: 2px; color: var(--ink-red);
    text-align: right; margin-top: 2px;
  }
  .card-front .contact {
    position: absolute; left: 48px; bottom: 30px; list-style: none;
    font-family: "Tinos", serif; font-size: 17px; line-height: 1.3; color: var(--ink-dark);
  }
</style>
</head>
<body>
<main class="canvas">
  <section class="card card-back">
    <div class="portrait" role="img" aria-label="Close-up photograph of red glossy lips"></div>
    <div class="write-line first"></div>
    <div class="write-line second"></div>
  </section>

  <section class="card card-front">
    <div class="lipstick" role="img" aria-label="Illustration of an open red lipstick"></div>
    <div class="identity">
      <h1 class="name">Alina Qasmi</h1>
      <div class="name-rule"></div>
      <p class="role">Makeup Artist</p>
    </div>
    <ul class="contact">
      <li>+92-300-5550-147</li>
      <li>alinaqasmi@mail.com</li>
      <li>www.alinaqasmi-studio.com</li>
    </ul>
  </section>
</main>
</body>
</html>
```